Graphic Design for Dating Site

I am looking for these words in dark or light grey color in a bold but simple font. They will be going in-between the attached brindlevault picture.
Display on a black background.

Where The Elite Meet

Date Wealth. Date Beauty

Make Global Connections

(Gold Tick Symbol on left that matches gold used in logo) and then the words '100% Secure Website'

```html
<!DOCTYPE html>
<html lang="en">
<head>
<meta charset="utf-8">
<title>Aurelia Club – Header</title>
<link href="https://fonts.googleapis.com/css2?family=Questrial&display=swap" rel="stylesheet">
<style>
  :root {
    --black: #000000;
    --gold-dark: #8a5a1c;
    --gold: #c8953f;
    --gold-light: #f3dc98;
    --text-grey: #a9a9a9;
    --nav-bg: #ffffff;
    --nav-text: #222222;
    --nav-line: #e4e4e4;
    --nav-border: #d8d8d8;
  }
  * { margin: 0; padding: 0; box-sizing: border-box; }
  html, body { width: 1200px; height: 307px; overflow: hidden; background: var(--black); }
  .header {
    position: relative;
    width: 1200px;
    height: 307px;
    font-family: "Questrial", sans-serif;
    background: var(--black);
  }
  .gold-band {
    position: absolute; left: 0; top: 0; width: 1200px; height: 14px;
    background: linear-gradient(90deg, var(--gold-dark) 0%, var(--gold-light) 12%, var(--gold) 30%,
      var(--gold-light) 48%, var(--gold-dark) 62%, var(--gold-light) 80%, var(--gold) 92%, var(--gold-light) 100%);
  }
  .secure-badge {
    position: absolute; left: 82px; top: 88px; width: 86px; height: 86px;
  }
  .secure-label {
    position: absolute; left: 24px; top: 181px; width: 210px;
    font-size: 19.5px; letter-spacing: 0.2px; color: var(--text-grey);
    text-transform: uppercase; white-space: nowrap;
  }
  .brand {
    position: absolute; left: 400px; top: 44px; width: 400px; text-align: center;
    color: var(--gold);
  }
  .brand-dot {
    display: block; margin: 0 auto 14px; width: 86px; height: 86px;
    border-radius: 50%; border: 3px solid var(--gold);
  }
  .brand-name {
    display: block; font-size: 40px; line-height: 40px; letter-spacing: 1px; text-transform: uppercase;
  }
  .brand-sub {
    display: block; font-size: 23px; line-height: 26px; letter-spacing: 14px; margin-left: 14px;
    text-transform: uppercase;
  }
  .tagline-frame { position: absolute; left: 835px; top: 68px; width: 320px; height: 133px; }
  .ornament {
    position: absolute; left: 68px; width: 184px; height: 28px;
    background: radial-gradient(ellipse at center, var(--gold-light) 0%, var(--gold) 45%, rgba(138,90,28,0) 75%);
  }
  .ornament.top { top: 0; }
  .ornament.bottom { top: 103px; }
  .frame-line {
    position: absolute; left: 0; width: 320px; height: 2px;
    background: linear-gradient(90deg, var(--gold-dark), var(--gold-light) 50%, var(--gold-dark));
  }
  .frame-line.top { top: 26px; }
  .frame-line.bottom { top: 104px; }
  .tagline {
    position: absolute; left: 0; top: 30px; width: 320px; text-align: center;
    color: var(--text-grey); text-transform: uppercase; font-size: 23.5px; line-height: 22.5px;
    white-space: nowrap;
  }
  .nav {
    position: absolute; left: 0; top: 264px; width: 1200px; height: 43px;
    background: var(--nav-bg); border-bottom: 4px solid var(--nav-border);
  }
  .nav-menu { position: absolute; left: 64px; top: 0; display: flex; list-style: none; height: 39px; }
  .nav-menu li {
    display: flex; align-items: center; justify-content: center; height: 39px;
    border-left: 1px solid var(--nav-line);
    font-size: 14px; color: var(--nav-text); text-transform: uppercase;
  }
  .nav-menu li:last-child { border-right: 1px solid var(--nav-line); }
  .nav-menu .home { width: 66px; }
  .nav-menu .about { width: 72px; }
  .nav-menu .benefits { width: 87px; }
  .nav-menu .news { width: 65px; }
  .nav-menu .search { width: 78px; }
  .auth-button {
    position: absolute; top: 7px; height: 26px; background: var(--black); color: #fff;
    font-size: 14px; font-weight: bold; display: flex; align-items: center; justify-content: center;
  }
  .auth-button.login { left: 991px; width: 62px; }
  .auth-button.signup { left: 1064px; width: 74px; }
</style>
</head>
<body>
<header class="header">
  <div class="gold-band"></div>

  <svg class="secure-badge" viewBox="0 0 86 86" aria-hidden="true">
    <defs>
      <linearGradient id="badgeGold" x1="0" y1="0" x2="1" y2="1">
        <stop offset="0" stop-color="#f3dc98"/>
        <stop offset="0.5" stop-color="#c8953f"/>
        <stop offset="1" stop-color="#8a5a1c"/>
      </linearGradient>
    </defs>
    <circle cx="43" cy="43" r="41" fill="url(#badgeGold)"/>
    <circle cx="43" cy="43" r="34" fill="#000"/>
    <circle cx="43" cy="43" r="31" fill="none" stroke="url(#badgeGold)" stroke-width="1.5"/>
    <path d="M26 43 L38 56 L62 28" fill="none" stroke="url(#badgeGold)" stroke-width="9" stroke-linecap="round" stroke-linejoin="round"/>
  </svg>
  <div class="secure-label">%100 Secure Website</div>

  <div class="brand">
    <span class="brand-dot"></span>
    <span class="brand-name">Aurelia</span>
    <span class="brand-sub">Club</span>
  </div>

  <div class="tagline-frame">
    <div class="ornament top" role="img" aria-label="Gold scrollwork flourish above the tagline"></div>
    <div class="frame-line top"></div>
    <p class="tagline">Where the elite meet<br>Date wealth . Date beauty<br>Make global connections</p>
    <div class="frame-line bottom"></div>
    <div class="ornament bottom" role="img" aria-label="Gold scrollwork flourish below the tagline"></div>
  </div>

  <nav class="nav">
    <ul class="nav-menu">
      <li class="home">Home</li>
      <li class="about">About</li>
      <li class="benefits">Benefits</li>
      <li class="news">News</li>
      <li class="search">Search</li>
    </ul>
    <span class="auth-button login">Login</span>
    <span class="auth-button signup">Sign up</span>
  </nav>
</header>
</body>
</html>
```